Professional Report Cover

We need a cover for CFO report (the document is about 20 pages, in case you decide to provide 3D mockup). The design must be professional. The main color has to be #299FC0, which can be incorporated with white, #375172, and #E3E7EE. See attached for content and logo.

```html
<!DOCTYPE html>
<html lang="en">
<head>
<meta charset="utf-8">
<title>The CFO Insight — Report Cover</title>
<link rel="stylesheet" href="https://fonts.googleapis.com/css2?family=Roboto:wght@400;500;700&display=swap">
<style>
  :root {
    --teal: #299FC0;
    --navy: #375172;
    --mist: #E3E7EE;
    --white: #FFFFFF;
    --ink: #1F2A36;
  }
  html, body {
    margin: 0;
    padding: 0;
    overflow: hidden;
    background: var(--white);
  }
  .cover {
    position: relative;
    width: 802px;
    height: 1200px;
    overflow: hidden;
    background: var(--white);
    font-family: "Roboto", Arial, sans-serif;
  }
  .title-band {
    position: absolute;
    left: 0; top: 0;
    width: 802px; height: 548px;
    background: var(--navy);
  }
  .title {
    position: absolute;
    left: 0; top: 18px;
    width: 802px;
    margin: 0;
    text-align: center;
    color: var(--white);
    font-weight: 500;
    font-size: 172px;
    line-height: 158px;
    letter-spacing: -1px;
  }
  .title span { display: block; }
  .hero-image {
    position: absolute;
    left: 0; top: 548px;
    width: 802px; height: 214px;
    background:
      radial-gradient(ellipse 260px 180px at 42% 45%, rgba(170, 215, 245, 0.55), rgba(170, 215, 245, 0) 70%),
      linear-gradient(100deg, #0F2A4A 0%, #1D4E80 40%, #2D7FB8 70%, #13365E 100%);
  }
  .contents-band {
    position: absolute;
    left: 0; top: 762px;
    width: 802px; height: 240px;
    background: var(--teal);
    color: var(--white);
    text-align: center;
  }
  .contents-heading {
    margin: 18px 0 4px;
    font-size: 15px;
    font-weight: 700;
    letter-spacing: 0.5px;
  }
  .contents-list {
    list-style: none;
    margin: 0;
    padding: 0;
    font-size: 15.5px;
    font-weight: 500;
    line-height: 21px;
  }
  .contents-list li { margin-bottom: 18px; }
  .contents-list li.tight { margin-bottom: 18px; }
  .brand {
    position: absolute;
    left: 0; top: 1050px;
    width: 802px;
    text-align: center;
    color: var(--navy);
  }
  .brand-name {
    display: inline-flex;
    align-items: center;
    gap: 10px;
    font-size: 22px;
    font-weight: 700;
    letter-spacing: 1px;
    text-transform: uppercase;
  }
  .brand-mark {
    width: 16px; height: 16px;
    background: var(--navy);
  }
  .brand-tagline {
    margin-top: 8px;
    font-size: 10px;
    font-weight: 700;
    letter-spacing: 1.5px;
    text-transform: uppercase;
  }
</style>
</head>
<body>
  <main class="cover">
    <header class="title-band">
      <h1 class="title"><span>The</span><span>CFO</span><span>Insight</span></h1>
    </header>

    <div class="hero-image" role="img" aria-label="Businessman in a suit wearing a virtual reality headset labelled CFO, surrounded by glowing blue digital interface graphics"></div>

    <section class="contents-band">
      <p class="contents-heading">INCLUDES:</p>
      <ul class="contents-list">
        <li>Insight into external, enterprise and departmental challenges</li>
        <li>Best practices and strategies to solve these challenges, with a focus<br>on innovation, securing competitive advantage and opportunities for growth</li>
        <li>Finance industry trends in the 2020s</li>
        <li>The leading role of CFOs in business transformation</li>
      </ul>
    </section>

    <footer class="brand">
      <div class="brand-name"><span class="brand-mark"></span>Northline Document Solutions</div>
      <div class="brand-tagline">A Meridian Group Company</div>
    </footer>
  </main>
</body>
</html>
```